Food Menu Design for Japanese Restaurant

Design a food menu for a high-end Japanese food restaurant. See attached detailed requirements file and menu items.

Industry/Entity Type

Restaurant

Colors

Designer to choose colors to be used in the design.

Requirements
Must have
• All menu items, descriptions, prices, add-ons, as provided in requirements file, all shown on designed menu and formatted.

```html
<!DOCTYPE html>
<html lang="en">
<head>
<meta charset="utf-8">
<title>Namiko — Starters, Soup &amp; Salad</title>
<link href="https://fonts.googleapis.com/css2?family=Lato:ital,wght@0,300;0,400;0,700;1,700;1,900&display=swap" rel="stylesheet">
<style>
  :root {
    --navy: #0f3759;
    --ink: #ffffff;
    --bloom: #8fa6d8;
  }
  * { margin: 0; padding: 0; box-sizing: border-box; }
  html, body { width: 1200px; height: 2394px; overflow: hidden; background: var(--navy); }
  .menu {
    position: relative;
    width: 1200px;
    height: 2394px;
    background: var(--navy);
    color: var(--ink);
    font-family: "Lato", sans-serif;
    overflow: hidden;
  }
  .blooms { position: absolute; inset: 0; pointer-events: none; }
  .section-title {
    position: absolute;
    font-weight: 400;
    font-size: 96px;
    line-height: 1;
    letter-spacing: 1px;
  }
  .item { position: absolute; }
  .col-left { left: 142px; width: 440px; }
  .col-right { left: 620px; width: 545px; }
  .col-salad { left: 620px; width: 400px; }
  .item-name { font-size: 27px; font-weight: 400; line-height: 31px; white-space: nowrap; }
  .item-desc {
    font-size: 14px;
    font-weight: 700;
    font-style: italic;
    line-height: 18px;
  }
  .item-desc b { font-weight: 900; }
  .item-price { font-size: 27px; font-weight: 400; line-height: 32px; margin-top: 2px; }
  .variant { margin-top: 8px; }
  .brand {
    position: absolute;
    left: 730px;
    top: 2192px;
    font-size: 60px;
    font-weight: 300;
    letter-spacing: 10px;
    line-height: 1;
  }
</style>
</head>
<body>
<main class="menu">

  <svg class="blooms" width="1200" height="2394" viewBox="0 0 1200 2394" role="img" aria-label="Faint chrysanthemum flower decorations along the right edge">
    <defs>
      <radialGradient id="bloomFade" cx="50%" cy="50%" r="50%">
        <stop offset="0%" stop-color="#8fa6d8" stop-opacity="0.35"/>
        <stop offset="100%" stop-color="#8fa6d8" stop-opacity="0"/>
      </radialGradient>
    </defs>
    <circle cx="1100" cy="60" r="140" fill="url(#bloomFade)"/>
    <circle cx="990" cy="-10" r="90" fill="url(#bloomFade)"/>
    <circle cx="1170" cy="280" r="95" fill="url(#bloomFade)"/>
    <circle cx="280" cy="70" r="70" fill="url(#bloomFade)"/>
    <circle cx="1180" cy="1480" r="75" fill="url(#bloomFade)"/>
  </svg>

  <h1 class="section-title" style="left:138px; top:118px;">STARTERS</h1>

  <!-- Starters, left column -->
  <div class="item col-left" style="top:251px;">
    <div class="item-name">Edamame</div>
    <div class="item-desc"><b>STEAMED:</b> Soybeans, Salted</div>
    <div class="item-price">5</div>
    <div class="variant">
      <div class="item-desc"><b>SPICY:</b> Soybeans, Sautéed With Sesame Oil<br>&amp; Sea Salt</div>
      <div class="item-price">6</div>
    </div>
  </div>

  <div class="item col-left" style="top:447px;">
    <div class="item-name">Shishito Peppers</div>
    <div class="item-desc">Sautéed</div>
    <div class="item-price">8</div>
  </div>

  <div class="item col-left" style="top:541px;">
    <div class="item-name">Agedashi Tofu</div>
    <div class="item-desc">Fried With Scallions, Bonito Flakes, Dashi Sauce</div>
    <div class="item-price">8</div>
  </div>

  <div class="item col-left" style="top:635px;">
    <div class="item-name">Spicy Rock Shrimp</div>
    <div class="item-desc">Tempura Battered Squid Tossed With Shichimi Pepper<br>Powder, With Spicy Aioli Sauce</div>
    <div class="item-price">12</div>
  </div>

  <div class="item col-left" style="top:753px;">
    <div class="item-name">Shrimp Shumai</div>
    <div class="item-desc">Shrimp Dumplings Served Steamed Or Deep Fried<br>With A Seasoned Soy Dipping Sauce</div>
    <div class="item-price">7</div>
  </div>

  <div class="item col-left" style="top:940px;">
    <div class="item-name">Gyoza</div>
    <div class="item-desc"><b>Pork:</b> Japanese Dumplings With Tofu, Bean Sprouts,<br>Chives Steamed Or Deep Fried</div>
    <div class="item-price">8</div>
    <div class="variant">
      <div class="item-desc"><b>Vegetable:</b> Japanese Dumplings With Shiitake<br>Mushrooms, Spinach, Leeks, Edamame<br>Steamed Or Deep Fried</div>
      <div class="item-price">7</div>
    </div>
  </div>

  <div class="item col-left" style="top:1185px;">
    <div class="item-name">Takoyaki</div>
    <div class="item-desc">Octopus Dumplings With Takoyaki Sauce, Japanese<br>Mayonnaise, And Bonito Flakes</div>
    <div class="item-price">6</div>
  </div>

  <div class="item col-left" style="top:1318px;">
    <div class="item-name">Namiko Wings</div>
    <div class="item-desc">Chicken Drummettes, Spicy Chili Sauce, Sesame Seeds</div>
    <div class="item-price">10</div>
  </div>

  <!-- Starters, right column -->
  <div class="item col-right" style="top:251px;">
    <div class="item-name">Tuna Tartare</div>
    <div class="item-desc">Seasoned tuna served with cucumber slices, masago</div>
    <div class="item-desc"><b>Tuna</b></div>
    <div class="item-price">14</div>
    <div class="variant">
      <div class="item-desc"><b>O Toro Tuna</b></div>
      <div class="item-price">21</div>
    </div>
  </div>

  <div class="item col-right" style="top:447px;">
    <div class="item-name">Tuna tataki</div>
    <div class="item-desc">seared Ahi tuna served with seaweed salad, ponzu</div>
    <div class="item-price">13</div>
  </div>

  <div class="item col-right" style="top:571px;">
    <div class="item-name">Soft shell crab</div>
    <div class="item-desc">deep fried in light batter and served with ponzu<br>dipping sauce</div>
    <div class="item-price">9</div>
  </div>

  <div class="item col-right" style="top:695px;">
    <div class="item-name">Carpaccio</div>
    <div class="item-desc">Lorem ipsum dolor sit amet, consectetur adipiscing<br>elit</div>
    <div class="item-price">X</div>
  </div>

  <div class="item col-right" style="top:825px;">
    <div class="item-name">Oysters</div>
    <div class="item-desc">"Namiko" type oysters, raw, shucked and served on the<br>half shell</div>
    <div class="item-desc">1 dozen</div>
    <div class="item-price">X</div>
    <div class="variant">
      <div class="item-desc">1/2 dozen</div>
      <div class="item-price">X</div>
    </div>
  </div>

  <div class="item col-right" style="top:1055px;">
    <div class="item-name">Chawanmushi</div>
    <div class="item-desc">Lorem ipsum dolor sit amet, consectetur adipiscing<br>elit</div>
    <div class="item-price">X</div>
  </div>

  <div class="item col-right" style="top:1185px;">
    <div class="item-name">Shrimp &amp; Vegetable Tempura</div>
    <div class="item-desc">shrimp &amp; seasonal vegetables fried tempura style</div>
    <div class="item-price">11</div>
  </div>

  <!-- Soup -->
  <h2 class="section-title" style="left:138px; top:1478px;">SOUP</h2>

  <div class="item col-left" style="top:1590px;">
    <div class="item-name">Miso Soup</div>
    <div class="item-desc"><b>Original:</b> silken tofu and scallions in miso broth</div>
    <div class="item-price">3</div>
    <div class="variant">
      <div class="item-desc"><b>Little neck clam miso:</b> Lorem ipsum dolor sit amet,<br>consectetur adipiscing elit</div>
      <div class="item-price">X</div>
    </div>
  </div>

  <div class="item col-left" style="top:1793px;">
    <div class="item-name">Dobin Mushi pot soup</div>
    <div class="item-desc">Lorem ipsum dolor sit amet, consectetur adipiscing elit</div>
    <div class="item-price">X</div>
  </div>

  <div class="item col-left" style="top:1905px;">
    <div class="item-name">Kabocha Pumpkin soup</div>
    <div class="item-desc">creamy Asian pumpkin with a mild ginger aroma</div>
    <div class="item-price">6</div>
  </div>

  <!-- Salad -->
  <h2 class="section-title" style="left:616px; top:1478px;">SALAD</h2>

  <div class="item col-salad" style="top:1590px;">
    <div class="item-name">Ahi tuna tataki salad</div>
    <div class="item-desc">thinly sliced seared ahi tuna served on a bed of mixed<br>greens, avocado, signature sesame dressing</div>
    <div class="item-price">14</div>
  </div>

  <div class="item col-salad" style="top:1726px;">
    <div class="item-name">Lobster and scallop salad</div>
    <div class="item-desc">Lorem ipsum dolor sit amet, consectetur adipiscing elit</div>
    <div class="item-price">X</div>
  </div>

  <div class="item col-salad" style="top:1829px;">
    <div class="item-name">Seaweed Salad</div>
    <div class="item-desc">fresh shredded seaweed in a chilled sesame vinaigrette</div>
    <div class="item-price">6</div>
  </div>

  <div class="item col-salad" style="top:1935px;">
    <div class="item-name">House Salad</div>
    <div class="item-desc">mixed greens with signature sesame dressing</div>
    <div class="item-price">5</div>
  </div>

  <div class="brand">namiko</div>

</main>
</body>
</html>
```